Kem7Dex Letterhead

Need a new letterhead for my law firm.
IDENTIFYING INFORMATION BELOW:
Ansel T Brightwater III
Attorney at Law
Address: 4832 Tillbury Rd, Ste 250, Dallas, TX 75204
Phone: 866-402-7183
Fax: 469-583-0271
Email: kem@kem7dex.example
Website: www.kem7dex.example

Colors
0054AA
0677BA
7BADD7
CADEEF
E8F1F8

Requirements
Must have
• Logo needs to be on the letterhead, along with identifying information which is included in the project description.

```html
<!DOCTYPE html>
<html lang="en">
<head>
<meta charset="utf-8">
<title>Kem7Dex Stationery</title>
<link href="https://fonts.googleapis.com/css2?family=Montserrat:wght@300;800&family=Roboto:ital,wght@0,400;0,700;1,400&display=swap" rel="stylesheet">
<style>
:root{
  --bg:#404f52;
  --teal:#4a8796;
  --royal:#0a55d6;
  --navy:#0e4a95;
  --sky:#3fd2ff;
  --sky-mid:#2fb0ea;
  --paper:#e8eeed;
  --ink:#111;
  --grey:#c8cbcb;
  --soft-grey:#c4cccc;
  --label:#e8f1f8;
}
*{margin:0;padding:0;box-sizing:border-box}
html,body{width:1200px;height:849px;overflow:hidden;background:var(--bg)}
body{position:relative;font-family:'Roboto',sans-serif}
.abs{position:absolute}
.backdrop{position:absolute;inset:0}
.label{position:absolute;font-family:'Montserrat',sans-serif;font-weight:300;font-size:13px;letter-spacing:1.2px;color:var(--label);white-space:nowrap}
.label.vertical{transform:rotate(-90deg);transform-origin:left top}
.wordmark{font-family:'Montserrat',sans-serif;font-weight:800;letter-spacing:.5px;line-height:1;white-space:nowrap}
.tagline{font-family:'Montserrat',sans-serif;font-weight:300;letter-spacing:1px;line-height:1;white-space:nowrap}
.shadow{box-shadow:4px 5px 10px rgba(0,0,0,.35)}

.cover{left:184px;top:114px;width:313px;height:404px;background:linear-gradient(170deg,var(--royal),var(--navy));overflow:hidden}
.cover .brand{position:absolute;left:0;right:0;top:134px;text-align:center;color:#fff}
.cover .wordmark{font-size:23px}
.cover .tagline{font-size:11px;margin-top:4px}

.folder{left:291px;top:286px;width:618px;height:412px;background:var(--sky)}
.folder .spine{position:absolute;left:309px;top:0;width:309px;height:100%;background:#38b4dc}

.contact{font-size:4.4px;line-height:7.1px}
.contact b{display:inline-block;width:8px;font-weight:700}
.office{font-weight:700;font-size:5.2px}

.card{width:118px;height:72px;overflow:hidden}
.card-front{left:438px;top:316px;background:var(--paper)}
.card-back{left:438px;top:406px;background:var(--sky);text-align:center}

.letterhead{left:688px;top:110px;width:313px;height:404px;background:var(--paper);overflow:hidden;color:var(--ink)}
.lh-body{position:absolute;left:25px;width:184px;font-size:4.1px;line-height:7.15px;text-align:justify;font-weight:700}
.lh-body .lead{color:var(--sky-mid);font-weight:400}
.highlight{position:absolute;left:224px;top:186px;font-weight:700;font-size:8px;line-height:8.2px;color:var(--royal)}
.highlight span{color:var(--sky-mid)}
.practice{position:absolute;left:224px;top:294px;color:#c9d0d0;font-size:7.4px;line-height:8px}
.practice h4{font-size:8px;font-weight:700;margin-bottom:4px}

.envelope{left:688px;top:604px;width:313px;height:170px;background:var(--sky);overflow:hidden}
</style>
</head>
<body>

<svg class="backdrop" width="1200" height="849" viewBox="0 0 1200 849" aria-hidden="true">
  <polygon points="0,0 950,0 830,110 690,150 0,0" fill="var(--teal)" opacity=".75"/>
  <polygon points="0,0 120,0 330,150 0,30" fill="var(--teal)" opacity=".45"/>
  <polygon points="690,150 950,0 830,110" fill="#4b7f8c" opacity=".6"/>
  <polygon points="160,849 700,720 1200,760 1200,849" fill="var(--teal)" opacity=".55"/>
  <polygon points="975,849 1088,773 1200,849" fill="#4d95a8" opacity=".9"/>
</svg>

<div class="label" style="left:710px;top:56px">letterhead</div>
<svg class="abs" style="left:689px;top:60px" width="6" height="6" aria-hidden="true"><polygon points="0,0 6,0 6,6" fill="#fff"/></svg>

<div class="label vertical" style="left:141px;top:497px">cover letter</div>
<svg class="abs" style="left:144px;top:512px" width="6" height="6" aria-hidden="true"><polygon points="0,0 6,0 0,6" fill="#fff"/></svg>

<div class="label vertical" style="left:396px;top:425px">name card</div>
<svg class="abs" style="left:398px;top:440px" width="6" height="6" aria-hidden="true"><polygon points="0,0 6,0 0,6" fill="#fff"/></svg>

<div class="label vertical" style="left:248px;top:673px">folder</div>
<svg class="abs" style="left:251px;top:688px" width="6" height="6" aria-hidden="true"><polygon points="0,0 6,0 0,6" fill="#fff"/></svg>

<div class="label vertical" style="left:1025px;top:714px">envelope</div>
<svg class="abs" style="left:1028px;top:729px" width="6" height="6" aria-hidden="true"><polygon points="0,0 6,0 0,6" fill="#fff"/></svg>

<!-- Folder -->
<div class="abs folder shadow">
  <div class="spine"></div>
  <svg class="abs" style="left:0;top:274px" width="618" height="138" viewBox="0 0 618 138" aria-hidden="true">
    <defs>
      <linearGradient id="pocketL" x1="0" x2="1"><stop offset="0" stop-color="var(--royal)"/><stop offset="1" stop-color="var(--navy)"/></linearGradient>
    </defs>
    <polygon points="0,0 286,0 301,138 0,138" fill="url(#pocketL)"/>
    <polygon points="175,0 225,0 227,17" fill="#2f8fd8" opacity=".8"/>
    <polygon points="195,0 240,0 227,17" fill="var(--sky)" opacity=".7"/>
    <polygon points="332,0 618,0 618,138 317,138" fill="url(#pocketL)"/>
    <polygon points="330,138 370,124 396,138" fill="#2f8fd8"/>
  </svg>
  <div class="abs" style="left:45px;top:292px;width:1px;height:56px;background:var(--sky)"></div>
  <div class="abs office" style="left:67px;top:326px;color:var(--sky)">DALLAS TEXAS OFFICE</div>
  <div class="abs contact" style="left:67px;top:357px;color:var(--sky)">
    <div><b>a :</b>4832 Tillbury Rd,</div>
    <div><b></b>Ste 250, Dallas, TX 75204</div>
    <div><b>p :</b>866-402-7183</div>
    <div><b>f :</b>469-583-0271</div>
    <div><b>e :</b>kem@kem7dex.example</div>
    <div><b>w :</b>www.kem7dex.example</div>
  </div>
</div>

<!-- Cover letter -->
<div class="abs cover shadow">
  <svg class="abs" style="left:0;top:0" width="313" height="404" viewBox="0 0 313 404" aria-hidden="true">
    <polygon points="163,0 313,0 283,27 218,27" fill="var(--sky)" opacity=".55"/>
    <polygon points="163,0 313,0 223,29" fill="#2f8fd8" opacity=".7"/>
    <polygon points="0,404 43,371 88,404" fill="#3ea0e6" opacity=".6"/>
    <polygon points="0,404 115,376 225,404" fill="#2f8fd8" opacity=".75"/>
  </svg>
  <div class="brand">
    <div class="wordmark">KEM7DEX</div>
    <div class="tagline">RIGHT ON YOUR SIDE</div>
  </div>
</div>

<!-- Name cards -->
<div class="abs card card-front shadow">
  <div class="abs" style="left:68px;top:0;width:1px;height:31px;background:var(--sky)"></div>
  <div class="abs" style="left:9px;top:22px;color:var(--ink)">
    <div class="wordmark" style="font-size:7px">KEM7DEX</div>
    <div class="tagline" style="font-size:2.6px;margin-top:1px">RIGHT ON YOUR SIDE</div>
  </div>
  <div class="abs" style="left:9px;top:37px;font-size:3.6px;line-height:5px">
    <div style="color:var(--royal);font-weight:700">Ansel T Brightwater III</div>
    <div style="color:var(--sky-mid);font-style:italic">Attorney at Law</div>
  </div>
  <div class="abs" style="left:74px;top:16px;font-size:3.2px;line-height:3.6px;font-weight:700;color:var(--royal)">DALLAS TEXAS<br><span style="color:var(--sky-mid)">OFFICE</span></div>
  <div class="abs" style="left:74px;top:27px;font-size:2.7px;line-height:4.9px;color:var(--royal)">
    <div>a : 4832 Tillbury Rd,</div>
    <div>&nbsp;&nbsp;&nbsp;Ste 250, Dallas,</div>
    <div>&nbsp;&nbsp;&nbsp;TX 75204</div>
    <div>p : 866-402-7183</div>
    <div>f : 469-583-0271</div>
    <div>e : kem@kem7dex.example</div>
  </div>
  <svg class="abs" style="left:0;top:64px" width="118" height="8" viewBox="0 0 118 8" aria-hidden="true">
    <polygon points="5,8 20,2 28,8" fill="var(--royal)"/>
    <polygon points="18,8 30,3 44,8" fill="var(--sky)"/>
  </svg>
</div>

<div class="abs card card-back shadow">
  <div style="margin-top:28px;color:var(--ink)">
    <div class="wordmark" style="font-size:11.5px">KEM7DEX</div>
    <div class="tagline" style="font-size:4.6px;margin-top:1px">RIGHT ON YOUR SIDE</div>
  </div>
</div>

<!-- Letterhead -->
<div class="abs letterhead shadow">
  <svg class="abs" style="left:0;top:0" width="313" height="404" viewBox="0 0 313 404" aria-hidden="true">
    <polygon points="29,0 84,0 56,16" fill="var(--sky)"/>
    <polygon points="29,0 73,0 40,8" fill="var(--royal)"/>
    <polygon points="100,404 128,392 153,404" fill="var(--royal)"/>
    <polygon points="136,404 162,394 212,404" fill="var(--sky)"/>
  </svg>
  <div class="abs" style="left:213px;top:0;width:1px;height:57px;background:var(--royal)"></div>

  <div class="abs" style="left:24px;top:38px">
    <div class="wordmark" style="font-size:14px">KEM7DEX</div>
    <div class="tagline" style="font-size:6.8px;margin-top:2px;padding-left:16px">RIGHT ON YOUR SIDE</div>
  </div>

  <div class="abs office" style="left:224px;top:38px;color:var(--royal)">DALLAS TEXAS <span style="color:var(--sky-mid)">OFFICE</span></div>
  <div class="abs contact" style="left:224px;top:68px;color:var(--royal);font-size:4.2px">
    <div><b>a :</b>4832 Tillbury Rd,</div>
    <div><b></b>Ste 250, Dallas, TX 75204</div>
    <div><b>p :</b>866-402-7183</div>
    <div><b>f :</b>469-583-0271</div>
    <div><b>e :</b>kem@kem7dex.example</div>
    <div><b>w :</b>www.kem7dex.example</div>
  </div>

  <div class="abs" style="left:25px;top:79px;font-size:5px;font-weight:700;color:var(--royal)">To : <span style="font-weight:400;color:var(--sky-mid)">Client's Name</span></div>
  <div class="abs contact" style="left:25px;top:90px;font-size:4.2px">
    <div><b>a :</b>client's address</div>
    <div><b>p :</b>client's contact</div>
    <div><b>e :</b>client's@email.com</div>
  </div>

  <div class="abs" style="left:25px;top:134px;font-size:5.6px;font-weight:700;color:var(--royal)">RE : Letterhead Design Template</div>
  <div class="abs" style="left:224px;top:135px;font-size:5px;color:var(--sky-mid)">05.01.2022</div>

  <p class="lh-body" style="top:161px"><span class="lead">Lorem ipsum dolor sit amet consectetuer odio non tellus natoque accumsan</span>. Sed hac enim Lorem tempus tortor justo eget scelerisque sed morbi. Senectus urna Vestibulum tincidunt turpis sem magna Nam hendrerit vitae nibh. Auctor Sed urna dignissim malesuada eleifend ultrices justo Curabitur Maecenas orci. Tincidunt adipiscing elit et et ac tincidunt elit nulla mauris eleifend. Urna. Quis ante odio consectetuer interdum eu dolor natoque Nam libero mollis. Euismod lacus ut velit tellus malesuada velit Curabitur quis semper a. Egestas eros quis sapien eu nunc Pellentesque Nulla Aenean congue magna. Nibh felis Morbi id iaculis tellus laoreet molestie Curabitur lorem Proin. Elit consequat cursus lorem eu in diam tortor elit. Justo. Penatibus lacus leo elit semper tempor arcu facilisis tincidunt nulla enim.</p>

  <p class="lh-body" style="top:240px">Dolor semper pretium sem pellentesque senectus sem fames lacinia sagittis elit. Nam Nulla Quisque sagittis et turpis Donec justo eu In Lorem. Lacinia id semper id dictum malesuada dui Integer platea lorem Morbi. Neque Ut mauris ut ut urna dolor fringilla pharetra eget magna. Suspendisse metus diam ipsum habitasse dui quis Maecenas aliquam ultrices pede. Curabitur sem id tellus augue non nibh congue laoreet eros id. At tempor augue quis mauris purus enim et Lorem Vivamus metus. Wisi vitae Donec In eget ut lorem neque massa et rhoncus. Ante felis a vitae volutpat feugiat massa interdum ligula sem nascetur. Rhoncus turpis ipsum at lorem Nulla tristique quis consequat elit dui. Urna Donec felis velit vestibulum libero vestibulum.</p>

  <div class="abs" style="left:25px;top:316px;font-size:4.3px;font-weight:700">yours sincerely,</div>
  <div class="abs" role="img" aria-label="Handwritten signature of Ansel T Brightwater III" style="left:27px;top:333px;width:48px;height:17px;background:linear-gradient(90deg,rgba(214,176,32,.55),rgba(214,176,32,.2));border-radius:3px"></div>
  <div class="abs" style="left:25px;top:356px;font-size:4.5px;line-height:6px">
    <div style="color:var(--royal);font-weight:700">Ansel T Brightwater III</div>
    <div style="color:var(--sky-mid);font-style:italic">Attorney at Law</div>
  </div>

  <div class="highlight"><span>ALLOCATED<br>FOR IMPORTANT/</span><br>HIGHLIGHT<br>INFORMATION</div>

  <div class="practice">
    <h4>PRACTICE AREAS</h4>
    <div>Cars / Trucks<br>Accidents</div>
    <div style="margin-top:4px">Premises Liability</div>
  </div>

  <div class="abs" style="left:224px;top:374px;width:89px;height:1px;background:var(--royal)"></div>
  <div class="abs" style="left:224px;top:384px;font-size:2.6px;color:var(--sky-mid)">Kem7Dex © All Rights Reserved - 2022</div>
</div>

<!-- Envelope -->
<div class="abs envelope shadow">
  <svg class="abs" style="left:0;top:0" width="313" height="170" viewBox="0 0 313 170" aria-hidden="true">
    <path d="M0,0 H313 V30 C300,55 288,73 260,73 H50 C25,73 8,55 0,30 Z" fill="var(--soft-grey)"/>
    <polygon points="0,0 170,0 80,29" fill="var(--sky)" opacity=".45"/>
    <polygon points="90,0 170,0 140,26" fill="var(--sky)" opacity=".55"/>
    <polygon points="89,170 190,140 313,170" fill="#2f8fd8" opacity=".75"/>
    <polygon points="222,170 255,138 313,170" fill="#1a6fd6" opacity=".85"/>
  </svg>
</div>

</body>
</html>
```